依頼詳細
<デザインイメージ>
・ラグジュアリー/高級なイメージ
・VIPのように扱われている
・希少な会に招待されている
記載項目
最低限記載項目:キャッチコピーや見出し/講演タイトル/日時/場所
※講演タイトル/日時/場所については、添付ファイルに記載しています。
※これを使って下さいという素材は特に決まっていません。
サイズ
A4
ページ数
片面
希望イメージ
• +5 0 +5
• シンプル
複雑
• 単色
カラフル
• 暗い
明るい
• 日常
高級
• 遊び心
厳粛
• 未来的
伝統的
• 女性的
男性的
希望する色
黄・オレンジ系、グレー系
納品ファイル
• 高解像度JPG (.jpg)
• イラストレーター形式 (.ai)
• フォトショップ形式 (.psd)
• PNG形式 (.png)
補足説明
依頼公開後の追記内容
<追記>

・講演の内容/テーマ
・講演のスケジュール
・会場について
・チケットの料金
・お申し込み方法
・お問い合わせ先

こちらについては
裏面に記載しております。

チラシ作品として非常に完成度が高かった事に加えて、内容も洗練されていたことが決め手となりました。

この度は、誠に多くのミルダー様にご提案をいただきましたことを、心から感謝いたします。皆様のご提案のクオリティがどれも高く選定にとても悩みました。

この度選定できなかったミルダー様にも、ご縁次第で、また直接ご依頼をさせていただきたいと思っておりますので、今後ともどうぞよろしくお願いいたします。

```html
<!DOCTYPE html>
<html lang="ja">
<head>
<meta charset="utf-8">
<title>来日講演 ビリオネアの授業 2018</title>
<link rel="stylesheet" href="https://fonts.googleapis.com/css2?family=Shippori+Mincho:wght@400;600;700;800&family=Cormorant+Garamond:wght@500;600&display=swap">
<style>
:root{
  --ink:#0b0b0c;
  --suit:#1d1e21;
  --shirt:#e9e8e4;
  --silver:#b9bbbe;
  --gold-light:#f6dd8e;
  --gold:#d5a84a;
  --gold-deep:#9b7127;
  --white:#f3f1ec;
  --muted:#bdb9b0;
}
*{margin:0;padding:0;box-sizing:border-box}
html,body{width:845px;height:1200px;overflow:hidden;background:var(--ink)}
.poster{
  position:relative;width:845px;height:1200px;overflow:hidden;
  background:radial-gradient(ellipse at 40% 40%,#26272a 0%,#141416 55%,var(--ink) 100%);
  font-family:"Shippori Mincho",serif;color:var(--white);
}
.hero-photo{
  position:absolute;left:0;top:0;width:845px;height:860px;
  background:
    radial-gradient(ellipse 70% 8% at 46% 88%,rgba(200,202,205,.55),rgba(120,122,125,.25) 60%,transparent 75%),
    linear-gradient(180deg,transparent 0 18%,rgba(233,232,228,.08) 18% 30%,transparent 30%),
    linear-gradient(90deg,#111214 0%,var(--suit) 30%,#2a2b2f 50%,var(--suit) 70%,#0f1012 100%);
  opacity:.9;
}
.hero-fade{
  position:absolute;left:0;top:700px;width:845px;height:500px;
  background:linear-gradient(180deg,transparent,var(--ink) 45%);
}
.tagline{
  position:absolute;right:28px;top:52px;
  writing-mode:vertical-rl;font-size:27px;line-height:1.55;letter-spacing:.12em;
  color:var(--white);font-weight:600;
}
.crown{
  position:absolute;left:360px;top:200px;width:128px;height:80px;
  background:linear-gradient(180deg,var(--gold-light),var(--gold) 55%,var(--gold-deep));
  border-radius:6px;opacity:.85;
}
.gold{
  background:linear-gradient(180deg,var(--gold-light) 0%,var(--gold) 55%,var(--gold-deep) 100%);
  -webkit-background-clip:text;background-clip:text;color:transparent;
}
.title-block{position:absolute;left:0;top:290px;width:845px;text-align:center}
.kicker{font-size:34px;font-weight:700;letter-spacing:.12em}
.title{font-size:98px;font-weight:700;line-height:1.15;letter-spacing:.02em;margin-top:4px;white-space:nowrap}
.title .line2{display:block;font-size:108px}
.year{font-family:"Cormorant Garamond",serif;font-size:44px;font-weight:600;letter-spacing:.45em;margin-top:6px;padding-left:.45em}
.info{position:absolute;left:135px;top:895px;width:620px}
.label{font-size:20px;font-weight:600;color:var(--white);letter-spacing:.05em;white-space:nowrap}
.label::before{content:"";display:inline-block;width:14px;height:14px;background:var(--white);margin-right:6px;vertical-align:-1px}
.rule{height:1px;background:var(--muted);opacity:.6;margin:6px 0 8px}
.content-text{font-size:24px;font-weight:700;letter-spacing:.02em;white-space:nowrap}
.details{display:flex;gap:26px;margin-top:36px}
.when{width:330px;flex:none}
.when .date{font-size:40px;font-weight:800;line-height:1.1;margin-top:4px;white-space:nowrap}
.when .date small{font-size:20px;font-weight:700;margin-left:2px}
.when .doors{font-size:15px;margin-top:8px;letter-spacing:.03em;white-space:nowrap}
.where{flex:1;min-width:0}
.where .venue{font-size:32px;font-weight:800;line-height:1.2;margin-top:6px;white-space:nowrap;letter-spacing:0}
.where .access{font-size:12px;color:var(--muted);margin-top:10px;letter-spacing:.02em;white-space:nowrap}
</style>
</head>
<body>
<main class="poster">
  <div class="hero-photo" role="img" aria-label="タキシード姿の執事が銀のトレーを差し出す写真"></div>
  <div class="hero-fade"></div>

  <p class="tagline">世界のビリオネアの<br>特別な授業を<br>特別な貴方に。</p>

  <div class="crown" role="img" aria-label="金色の王冠の装飾"></div>

  <header class="title-block">
    <p class="kicker gold">来日講演</p>
    <h1 class="title gold">ビリオネアの<span class="line2">授業</span></h1>
    <p class="year gold">2018</p>
  </header>

  <section class="info">
    <p class="label">講演内容</p>
    <div class="rule"></div>
    <p class="content-text">成功・リーダーシップ・桁違いの億万長者になるには</p>

    <div class="details">
      <div class="when">
        <p class="label">講演日時</p>
        <div class="rule"></div>
        <p class="date">2018 9/17<small>(月・祝)</small></p>
        <p class="doors">●開場 12:00〜　●開演 13:00〜19:30</p>
      </div>
      <div class="where">
        <p class="label">講演会場</p>
        <div class="rule"></div>
        <p class="venue">難波中央記念ホール</p>
        <p class="access">地下鉄中央線 北浜駅より徒歩5分　会場詳細は裏面</p>
      </div>
    </div>
  </section>
</main>
</body>
</html>
```